Dwight Ferrell Political Campaign Business Cards

Design business card that encorporated Texas Brevard Shire and my existing campaign. Somewhere on the card needs to have. Brevard Shire is in Texas and I am running for Brevard Shire Judge. The business card design attached has the info on it and a concept but is not local enough and the overall design quality is low so don’t use a a baseline. Not looking for modern anything, should have square for corners, running for Brevard Shire Judge.

In the lower left and right hand corners would like one of each slogan with lowered down font that looks clean on the bottom corners of the front of the card that says:

“Retired Staff Sergeant Northern Frontier Guard”
“KRT/BZN Veteran”

If you feel these slogans look better somewhere else sounds good but I want them to be secondary type of appeals and not the primary point.

Phone we can incorporate in as well:
503-248-1957

Facebook:
www.pagelinkhub.com/voteharbin

Website:
www.steadyplainsward.com

County website:

https://www.brevardshiregov.org/Pages/default.aspx

Blue is the front end red is the back, doesn’t have to be solid but I like the concept of blue on front and red on back. Not absolutely necessary if doesn’t fit design and what looks best.

Eliminate the phrase Conservative Democrat from the project

Two photos have been added to replace the BZN/KRT text. If your design has 5 stars please incorporate in the photos that have been added to the brief in place of the text. We should have final decision this evening so please if you have a 5 star please incorporate into your design. If the background color needs to change to make it work sounds good

Industry/Entity Type

Political

Contact Information for Business Card

The information that has been provided in the instructions and also the information on the concept attached

Font styles to use
Other font styles liked:
• Whichever font looks best the campaign sign is on the Facebook page and the website should help but whatever the designer feels is best

Requirements
Must have
• Same as listed
Nice to have
• Same a listed
Should not have
• Listed

```html
<!DOCTYPE html>
<html lang="en">
<head>
<meta charset="utf-8">
<title>Dwight Ferrell – Business Cards</title>
<link rel="stylesheet" href="https://fonts.googleapis.com/css2?family=Cinzel:wght@400;700;800&family=Open+Sans:wght@400;600&display=swap">
<style>
  :root {
    --backdrop: #e6e6e6;
    --paper: #ffffff;
    --campaign-red: #c8202c;
    --campaign-red-dark: #a51822;
    --campaign-blue: #23307a;
    --campaign-blue-dark: #1a2560;
    --ink: #1f1f1f;
  }
  * { margin: 0; padding: 0; box-sizing: border-box; }
  html, body {
    width: 800px; height: 1200px; overflow: hidden;
    background: var(--backdrop);
  }
  .canvas { position: relative; width: 800px; height: 1200px; }

  .card {
    position: absolute;
    left: 195px;
    width: 416px;
    height: 232px;
    padding: 14px;
  }
  .card--front { top: 312px; background: var(--campaign-red); }
  .card--back  { top: 653px; background: var(--campaign-blue); }

  .card__face {
    width: 100%; height: 100%;
    background: var(--paper);
    display: flex; flex-direction: column; align-items: center;
    text-align: center;
  }

  /* Front */
  .card--front .card__face { padding-top: 18px; }
  .star-row { display: flex; gap: 20px; align-items: center; height: 14px; }
  .star-row svg { width: 11px; height: 11px; fill: var(--campaign-blue); }
  .star-row .star-row__gap { width: 34px; }

  .campaign-mark { display: flex; flex-direction: column; align-items: center; margin-top: 4px; }
  .campaign-mark__disc {
    width: 36px; height: 36px; border-radius: 50%;
    background: var(--campaign-blue);
  }
  .campaign-mark__name {
    margin-top: 7px;
    font-family: "Cinzel", serif; font-weight: 700;
    font-size: 15px; letter-spacing: 1.5px; text-transform: uppercase;
    color: var(--campaign-red);
  }

  .service-lines { margin-top: 14px; }
  .service-lines p {
    font-family: "Cinzel", serif; font-weight: 400;
    font-size: 9.5px; letter-spacing: 0.4px;
    color: var(--ink); line-height: 1.7;
  }

  /* Back */
  .card--back .card__face { padding-top: 16px; }
  .candidate__disc {
    width: 34px; height: 34px; border-radius: 50%;
    background: var(--campaign-blue);
  }
  .candidate__name {
    margin-top: 5px;
    font-family: "Cinzel", serif; font-weight: 800;
    font-size: 19px; letter-spacing: 1px; line-height: 1;
    color: var(--campaign-blue);
  }
  .candidate__office {
    margin-top: 3px;
    background: var(--campaign-red);
    color: var(--paper);
    font-family: "Cinzel", serif; font-weight: 700;
    font-size: 7.5px; letter-spacing: 0.8px; text-transform: uppercase;
    padding: 2px 12px;
  }
  .contact { margin-top: 9px; list-style: none; }
  .contact li {
    font-family: "Open Sans", sans-serif; font-weight: 400;
    font-size: 8px; color: var(--ink); line-height: 1.9;
  }
</style>
</head>
<body>
<main class="canvas">

  <section class="card card--front" aria-label="Card front">
    <div class="card__face">
      <div class="star-row" aria-hidden="true">
        <svg viewBox="0 0 24 24"><path d="M12 1l3.1 7 7.6.6-5.8 5 1.8 7.4L12 17l-6.7 4 1.8-7.4-5.8-5 7.6-.6z"/></svg>
        <svg viewBox="0 0 24 24"><path d="M12 1l3.1 7 7.6.6-5.8 5 1.8 7.4L12 17l-6.7 4 1.8-7.4-5.8-5 7.6-.6z"/></svg>
        <span class="star-row__gap"></span>
        <svg viewBox="0 0 24 24"><path d="M12 1l3.1 7 7.6.6-5.8 5 1.8 7.4L12 17l-6.7 4 1.8-7.4-5.8-5 7.6-.6z"/></svg>
        <svg viewBox="0 0 24 24"><path d="M12 1l3.1 7 7.6.6-5.8 5 1.8 7.4L12 17l-6.7 4 1.8-7.4-5.8-5 7.6-.6z"/></svg>
        <svg viewBox="0 0 24 24"><path d="M12 1l3.1 7 7.6.6-5.8 5 1.8 7.4L12 17l-6.7 4 1.8-7.4-5.8-5 7.6-.6z"/></svg>
      </div>
      <div class="campaign-mark">
        <div class="campaign-mark__disc"></div>
        <div class="campaign-mark__name">Brevard Shire</div>
      </div>
      <div class="service-lines">
        <p>“Retired Staff Sergeant Northern Frontier Guard”</p>
        <p>“KRT/BZN Veteran”</p>
      </div>
    </div>
  </section>

  <section class="card card--back" aria-label="Card back">
    <div class="card__face">
      <div class="candidate__disc"></div>
      <h1 class="candidate__name">DWIGHT FERRELL</h1>
      <div class="candidate__office">For Brevard Shire Judge</div>
      <ul class="contact">
        <li>503-248-1957</li>
        <li>www.pagelinkhub.com/voteharbin</li>
        <li>www.steadyplainsward.com</li>
        <li>www.brevardshiregov.org</li>
      </ul>
    </div>
  </section>

</main>
</body>
</html>
```